Business card design needed

I need a business card design for a new online retail business based in Australia. I am unsure of the exact content of what I will be selling but it will be probably women's clothing, accessories, gym wear, gifts and maybe homeware linen. I am wanting a classy design that portrays the image of class/style/upmarket.

Target Market(s)

predominantely women - 20-50 age group

Industry/Entity Type

Retail

Contact Information for Business Card

Purely Lustre
Karen Whitlow
Director
ABN 73215548906
17 Harcourt Lane Dunmore Ridge NSW 2291
ph: +61 427 390 845
sales@purelylustre.com.au

Logo Text

I am open for suggestions here

Requirements
Must have
• The design must be both sides of the card

```html
<!DOCTYPE html>
<html lang="en">
<head>
<meta charset="utf-8">
<title>Purely Lustre – Business Card</title>
<link href="https://fonts.googleapis.com/css2?family=Cinzel:wght@400&family=Arimo:wght@400&display=swap" rel="stylesheet">
<style>
  :root {
    --backdrop: #e8e8e8;
    --burgundy: #5b1016;
    --gold: #f2b321;
    --card-w: 560px;
    --card-h: 340px;
  }
  * { margin: 0; padding: 0; box-sizing: border-box; }
  html, body {
    width: 1200px;
    height: 1000px;
    overflow: hidden;
    background: var(--backdrop);
  }
  .sheet {
    position: relative;
    width: 1200px;
    height: 1000px;
    display: flex;
    flex-direction: column;
    align-items: center;
    justify-content: center;
    gap: 60px;
  }
  .card {
    position: relative;
    width: var(--card-w);
    height: var(--card-h);
    background: var(--burgundy);
    color: var(--gold);
    box-shadow: 0 6px 18px rgba(0, 0, 0, 0.18);
  }

  /* Front side */
  .card--front {
    display: flex;
    flex-direction: column;
    align-items: center;
    justify-content: center;
  }
  .wordmark {
    font-family: "Cinzel", Georgia, serif;
    font-weight: 400;
    letter-spacing: 0.14em;
    color: var(--gold);
    display: flex;
    align-items: center;
    gap: 12px;
  }
  .wordmark__dot {
    width: 10px;
    height: 10px;
    border-radius: 50%;
    background: var(--gold);
  }
  .card--front .wordmark { font-size: 34px; }
  .website {
    margin-top: 22px;
    font-family: "Arimo", Arial, sans-serif;
    font-size: 12px;
    letter-spacing: 0.02em;
  }

  /* Back side */
  .card--back .wordmark {
    position: absolute;
    left: 40px;
    top: 46px;
    font-size: 20px;
    gap: 9px;
  }
  .card--back .wordmark__dot { width: 7px; height: 7px; }
  .details {
    position: absolute;
    left: 40px;
    right: 40px;
    top: 150px;
    display: grid;
    grid-template-columns: 1.15fr 1.2fr 0.8fr;
    column-gap: 18px;
    font-family: "Arimo", Arial, sans-serif;
    font-size: 11px;
    line-height: 1.35;
  }
  .person__name {
    font-size: 16px;
    letter-spacing: 0.03em;
    text-transform: uppercase;
  }
  .person__role { font-size: 10px; margin-bottom: 10px; }
  .label { text-transform: uppercase; margin-top: 8px; }
  .column--email, .column--abn { padding-top: 60px; }
</style>
</head>
<body>
<main class="sheet">
  <section class="card card--front" aria-label="Card front">
    <div class="wordmark"><span class="wordmark__dot"></span>PURELY LUSTRE</div>
    <p class="website">www.PurelyLustre.com.au</p>
  </section>

  <section class="card card--back" aria-label="Card back">
    <div class="wordmark"><span class="wordmark__dot"></span>PURELY LUSTRE</div>
    <div class="details">
      <div class="column column--person">
        <p class="person__name">Karen Whitlow</p>
        <p class="person__role">Director</p>
        <p class="address">17 Harcourt Lane Dunmore Ridge<br>NSW 2291</p>
        <p class="label">Phone</p>
        <p class="phone">+61 427 390 845</p>
      </div>
      <div class="column column--email">
        <p class="label">Email</p>
        <p class="email">sales@purelylustre.com.au</p>
      </div>
      <div class="column column--abn">
        <p class="label">ABN</p>
        <p class="abn">73215548906</p>
      </div>
    </div>
  </section>
</main>
</body>
</html>
```